Armpit White Cream Package Box Design

1. We need the package design of this armpit white cream, this is for whitening underarm or private area,bikini line.
2. The design should US or EU acceptable, simple and directly show the function and advantage with only one glimps.
3. Color base should be fresh light and attractive.
4. Picture couldn't infringement in any country.

```html
<!DOCTYPE html>
<html lang="en">
<head>
<meta charset="utf-8">
<title>Velora Underarm Bright Cream – Label</title>
<link rel="stylesheet" href="https://fonts.googleapis.com/css2?family=Montserrat:wght@400;600&display=swap">
<style>
  :root {
    --backdrop: #fbb29a;
    --label-blush: #fde3dc;
    --label-pink: #f6c6cc;
    --teal-deep: #12687a;
    --teal-bright: #17c9cc;
    --teal-soft: #6fd0d2;
    --coral: #f8837a;
    --coral-dark: #f06f6d;
    --ink-light: #ffffff;
  }
  * { margin: 0; padding: 0; box-sizing: border-box; }
  html, body {
    width: 1171px;
    height: 1200px;
    overflow: hidden;
    background: var(--backdrop);
    font-family: "Montserrat", sans-serif;
  }
  .canvas {
    position: relative;
    width: 1171px;
    height: 1200px;
  }
  .label {
    position: absolute;
    left: 368px;
    top: 219px;
    width: 432px;
    height: 656px;
    overflow: hidden;
    background: var(--label-blush);
  }
  .label-artwork {
    position: absolute;
    left: 0;
    top: 0;
    width: 432px;
    height: 500px;
    background:
      radial-gradient(ellipse 50% 40% at 8% 12%, var(--teal-deep) 0 60%, transparent 61%),
      radial-gradient(ellipse 40% 55% at 0% 62%, var(--teal-bright) 0 70%, transparent 71%),
      linear-gradient(90deg, var(--label-blush) 45%, var(--label-pink) 100%);
  }
  .accent-ring {
    position: absolute;
    left: 137px;
    top: 131px;
    width: 120px;
    height: 120px;
    border-radius: 50%;
    background: rgba(214, 160, 190, 0.55);
    border: 3px solid rgba(255, 255, 255, 0.6);
  }
  .accent-dot {
    position: absolute;
    left: 283px;
    top: 207px;
    width: 44px;
    height: 42px;
    border-radius: 50%;
    background: var(--teal-soft);
  }
  .zones-badge {
    position: absolute;
    left: 243px;
    top: 240px;
    width: 202px;
    height: 202px;
    border-radius: 50%;
    background: var(--teal-soft);
    color: var(--ink-light);
    font-size: 19px;
    font-weight: 400;
    line-height: 1.3;
    padding: 58px 0 0 36px;
    white-space: nowrap;
  }
  .name-band {
    position: absolute;
    left: 0;
    top: 471px;
    width: 432px;
    height: 185px;
  }
  .name-band svg { position: absolute; inset: 0; }
  .name-text {
    position: absolute;
    left: 78px;
    top: 46px;
    color: var(--ink-light);
  }
  .name-tag {
    font-size: 19px;
    font-weight: 400;
    line-height: 1.2;
    margin-bottom: 8px;
  }
  .name-title {
    font-size: 32px;
    font-weight: 600;
    line-height: 1.3;
  }
</style>
</head>
<body>
  <main class="canvas">
    <section class="label">
      <div class="label-artwork" role="img" aria-label="Abstract illustration of a raised arm and underarm in teal and blush shapes"></div>
      <div class="accent-ring"></div>
      <div class="accent-dot"></div>
      <div class="zones-badge">Underarm<br>Private area<br>Bikini line</div>
      <div class="name-band">
        <svg width="432" height="185" viewBox="0 0 432 185" aria-hidden="true">
          <path d="M0 25 C120 0 300 -5 432 20 L432 185 L0 185 Z" fill="var(--coral)"/>
          <path d="M280 50 C340 30 410 35 432 50 L432 140 C400 160 340 150 310 120 C280 90 262 65 280 50 Z" fill="var(--coral-dark)"/>
        </svg>
        <div class="name-text">
          <p class="name-tag">Velora</p>
          <h1 class="name-title">Underarm<br>Bright Cream</h1>
        </div>
      </div>
    </section>
  </main>
</body>
</html>
```